Re-design of current business cards

We are updating our website with new colors and layout. Would like to re-design our business cards to co-ordinate. See attached pdf with new Brindlecraft website colors. We would also like to combine our 2 brands on the one business card. Attached is the new design for our Brindlecraft website, current business cards, which are one sided, brindlecraft logo in tiff, .ai for fonts. Brindlecraft logo font is Optimum, Quillmarsh website home page image, Quillmarsh brand statics for products which includes the logo for this brand.

Quillmarsh brand will stay the dark gray on the website. See attached statics for product and website home page.
Updates

The business cards will be 2 sided. Brindlecraft Brand on one side and Quillmarsh Brand on the other. The colors for Brindlecraft need to follow the color scheme of the brindlecraft website pdf I uploaded. The colors are a blue, lighter teal blue and white. Quillmarsh needs to follow the dark gray color on files uploaded

Target Market(s)

The trade and consumers

Industry/Entity Type

Home Furnishing

Contact Information for Business Card

We are updating our website with new colors and layout. Would like to re-design our business cards to co-ordinate. We would also like to combine our 2 brands onto 1 2 sided business cards.

Requirements
Must have
• Colors that match our new website, see attached image.
• RGB colors
• navy -#152842
• teal - 98aeb9
• The gray color used for Quillmarsh brands.
• ll logos and fonts should stay the same.

```html
<!DOCTYPE html>
<html lang="en">
<head>
<meta charset="utf-8">
<title>Brindlecraft / Quillmarsh Business Card</title>
<link rel="stylesheet" href="https://fonts.googleapis.com/css2?family=Marcellus&family=Raleway:wght@400;800&family=Roboto+Condensed:wght@300&display=swap">
<style>
  :root {
    --paper: #ffffff;
    --quillmarsh-gray: #59595b;
    --brindle-navy: #152842;
    --brindle-teal: #98aeb9;
    --light-text: #e9e9ea;
    --contact-text: #ffffff;
    --edge: #000000;
  }
  * { margin: 0; padding: 0; box-sizing: border-box; }
  html, body {
    width: 1200px; height: 1200px; overflow: hidden;
    background: var(--paper);
  }
  .sheet { position: relative; width: 1200px; height: 1200px; }
  .card {
    position: absolute; left: 196px; width: 809px; height: 526px;
    border: 2.5px solid var(--edge); overflow: hidden;
  }
  .card--front { top: 46px; background: var(--quillmarsh-gray); }
  .card--back { top: 618px; background: var(--paper); }

  .brand-name--quillmarsh {
    position: absolute; left: 0; right: 0; top: 136px;
    text-align: center;
    font-family: "Marcellus", serif; font-size: 88px; line-height: 1;
    letter-spacing: -1px; color: var(--light-text);
  }
  .tagline {
    position: absolute; left: 0; right: 0; top: 300px;
    text-align: center;
    font-family: "Roboto Condensed", sans-serif; font-weight: 300;
    font-size: 37px; color: var(--light-text);
  }

  .brand-dot {
    position: absolute; left: 348px; top: 37px;
    width: 108px; height: 108px; border-radius: 50%;
    background: var(--brindle-teal);
  }
  .brand-name--brindlecraft {
    position: absolute; left: 0; right: 0; top: 152px;
    text-align: center;
    font-family: "Marcellus", serif; font-size: 78px; line-height: 1;
    letter-spacing: -1.5px; color: var(--brindle-navy);
  }
  .website {
    position: absolute; left: 0; right: 0; top: 246px;
    text-align: center;
    font-family: "Marcellus", serif; font-size: 19px;
    letter-spacing: 1px; color: var(--brindle-navy);
  }

  .contact-band {
    position: absolute; left: 0; right: 0; top: 334px; bottom: 0;
    background: var(--brindle-navy); color: var(--contact-text);
    font-family: "Raleway", sans-serif; font-size: 21px; line-height: 33.5px;
  }
  .person { position: absolute; left: 48px; top: 18px; }
  .person__name { font-weight: 800; font-size: 23px; }
  .office { position: absolute; right: 48px; top: 18px; text-align: right; }
  .office__phones span + span { margin-left: 30px; }
</style>
</head>
<body>
<main class="sheet">
  <section class="card card--front">
    <div class="brand-name--quillmarsh">QUILLMARSH</div>
    <p class="tagline">Discover the luxury of home.</p>
  </section>

  <section class="card card--back">
    <div class="brand-dot" aria-hidden="true"></div>
    <div class="brand-name--brindlecraft">BRINDLECRAFT</div>
    <p class="website">www.brindlecraft.com</p>

    <div class="contact-band">
      <div class="person">
        <div class="person__name">Dana Whitlow</div>
        <div>Graphics/</div>
        <div>Photography</div>
        <div>Director</div>
      </div>
      <div class="office">
        <div>P.O BOX 412/1870 Fernbrook RD</div>
        <div>Cedar Falls, Virginia 24099</div>
        <div class="office__phones"><span>P 555.201.4417</span><span>F555.201.4480</span></div>
        <div>Email: dwhitlow@brindlecraft.com</div>
      </div>
    </div>
  </section>
</main>
</body>
</html>
```